R7M Meridian Business Card Design

We need a business card created for our New Business "R7M Meridian"<br/><br/>The business card design is up to you however the following information must be on the business card:<br/><br/>Front of the business card -<br/>Email :dorianv@r7mmeridian.nz<br/>Mobile: +64 (0) 22 4871 659<br/>Website: www.r7mmeridian.nz<br/>Card Owner Name: Dorian Valcourt<br/>Company Title: Business Development Manager<br/>Slogan: "The BEST of both worlds". <br/>Logo On the front attached to the design brief<br/><br/>On the back: <br/>Space on the back for 4 more versions of the logo across the bottom of the card indicating different subsidiary brands - R7M Coffee, R7M Arts, R7M ?? (The card will be used for all of these brands - We Will add the extra subsidiary logos to the design once the design is finished (We are a graphics design team). <br/><br/>Other than that we want a premium feeling logo that remains universally usable depending on the business entity that we are using the card for. The use of bright bold colours would be great but we still want the card to feel premium.
Target Market(s)
Gift Design and Manufacturing Companies
Contact Information for Business Card
Front of the business card -
Email :dorianv@r7mmeridian.nz
Mobile: +64 (0) 22 4871 659
Website: www.r7mmeridian.nz
Card Owner Name: Dorian Valcourt
Company Title: Business Development Manager
Slogan: "The BEST of both worlds".
Logo On the front attached to the design brief

```html
<!DOCTYPE html>
<html lang="en">
<head>
<meta charset="utf-8">
<title>R7M Meridian Business Card</title>
<link rel="stylesheet" href="https://fonts.googleapis.com/css2?family=Montserrat:wght@600;700&family=Arimo:wght@400&display=swap">
<style>
  :root {
    --stage: #2f2f2f;
    --brand-blue: #36479e;
    --ink-blue: #2b3ca0;
    --ink: #1b1b1b;
    --paper: #ffffff;
    --rule: #cfcfcf;
  }
  * { margin: 0; padding: 0; box-sizing: border-box; }
  html, body { width: 1200px; height: 900px; overflow: hidden; }
  body { background: var(--stage); position: relative; font-family: "Arimo", Arial, sans-serif; }

  .card {
    position: absolute;
    top: 200px;
    width: 310px;
    height: 502px;
    box-shadow: 3px 4px 6px rgba(0,0,0,0.55);
  }
  .card--front {
    left: 253px;
    background: var(--paper);
    border-radius: 62px 0 62px 0;
  }
  .card--back {
    left: 627px;
    background: var(--brand-blue);
    border-radius: 0 62px 0 62px;
  }

  .brand-name {
    position: absolute;
    left: 0; right: 0;
    text-align: center;
    font-family: "Montserrat", sans-serif;
    font-weight: 700;
    font-size: 28px;
    line-height: 1;
    white-space: nowrap;
  }
  .card--front .brand-name { top: 140px; color: var(--ink-blue); }
  .card--back .brand-name { top: 216px; color: var(--paper); }

  .holder { position: absolute; left: 34px; top: 285px; }
  .holder__name {
    font-family: "Montserrat", sans-serif;
    font-weight: 700;
    font-size: 16.5px;
    color: var(--ink-blue);
    letter-spacing: 0.3px;
  }
  .holder__title { font-size: 14px; color: var(--ink); margin-top: 1px; }

  .contacts { position: absolute; left: 33px; top: 343px; list-style: none; }
  .contacts li {
    display: flex; align-items: center; gap: 4px;
    font-size: 14px; color: var(--ink); height: 19.5px;
  }
  .contacts svg { width: 15px; height: 15px; flex: none; }
  .contacts .accent { color: var(--ink-blue); }

  .rule { position: absolute; left: 32px; top: 416px; width: 242px; height: 1px; background: var(--rule); }

  .slogan {
    position: absolute; left: 0; right: 0; top: 434px;
    text-align: center;
    font-family: "Montserrat", sans-serif;
    font-weight: 700; font-size: 16.4px;
    color: var(--ink-blue);
  }

  .back-url {
    position: absolute; left: 0; right: 0; top: 444px;
    text-align: center;
    font-family: "Montserrat", sans-serif;
    font-weight: 600; font-size: 14px;
    color: var(--paper);
  }
</style>
</head>
<body>
  <section class="card card--front">
    <p class="brand-name">R7M Meridian</p>

    <div class="holder">
      <p class="holder__name">DORIAN VALCOURT</p>
      <p class="holder__title">Business Development Manager</p>
    </div>

    <ul class="contacts">
      <li>
        <svg viewBox="0 0 16 16"><rect x="1" y="1" width="14" height="14" rx="2" fill="none" stroke="#2b3ca0" stroke-width="1.4"/><path d="M5 4c-1 1-1 3 1.5 5.5S10.5 13 12 11.5l-1.6-1.6-1.3.8C8 10 6.5 8.5 5.8 7.4l.8-1.3z" fill="#2b3ca0"/></svg>
        +64 (0) 22 4871 659
      </li>
      <li>
        <svg viewBox="0 0 16 16"><rect x="1" y="3" width="14" height="10" fill="#2b3ca0"/><path d="M1 3l7 6 7-6" fill="none" stroke="#fff" stroke-width="1.2"/></svg>
        dorianv@r7mmeridian.nz
      </li>
      <li>
        <svg viewBox="0 0 16 16" fill="none" stroke="#2b3ca0" stroke-width="1.2"><circle cx="8" cy="8" r="6.5"/><ellipse cx="8" cy="8" rx="3" ry="6.5"/><path d="M1.5 8h13M2.5 5h11M2.5 11h11"/></svg>
        <span>www.<span class="accent">r7mmeridian</span>.nz</span>
      </li>
    </ul>

    <div class="rule"></div>
    <p class="slogan">THE BEST OF BOTH WORLDS</p>
  </section>

  <section class="card card--back">
    <p class="brand-name">R7M Meridian</p>
    <p class="back-url">www.r7mmeridian.nz</p>
  </section>
</body>
</html>
```